Bytemill - a software development company requires letter head

I currently have a business card and logo, I just need a nice looking letter head the matches the two. I will upload these Illustrator files.

I would like the letter head to be done in a current version of MS Word.

Please incorporate 'bytemill' as per the attached font and the logo.

Industry/Entity Type

Computer Software

Colors

Designer to choose colors to be used in the design.

Requirements
Must have
• Fits in with current design, sleek and professional. It will be used for quotations and tenders and documentation going to clients and potential clients.
• Would like to company logo up the top header and perhaps a watermark of the logo at the bottom right, a bit like the business card.
• Also it needs to be MS word.
• Please work with the color pallet from the attached files.

```html
<!DOCTYPE html>
<html lang="en">
<head>
<meta charset="utf-8">
<title>Bytemill Letterhead</title>
<link href="https://fonts.googleapis.com/css2?family=Exo+2:wght@500&family=Raleway:wght@400&display=swap" rel="stylesheet">
<style>
  :root {
    --backdrop: #3a3a3a;
    --paper: #f4f5f6;
    --brand-blue: #2d9bd6;
    --deep-blue: #1b4fa8;
    --mid-blue: #2a7cc8;
    --light-blue: #5cc0e0;
    --ink: #3d3f42;
  }
  html, body {
    margin: 0;
    width: 1200px;
    height: 1200px;
    overflow: hidden;
    background: var(--backdrop);
  }
  .canvas {
    position: relative;
    width: 1200px;
    height: 1200px;
  }
  .letterhead {
    position: absolute;
    left: 204px;
    top: 40px;
    width: 792px;
    height: 1120px;
    background: linear-gradient(160deg, #ffffff 0%, var(--paper) 60%, #e9eaeb 100%);
    box-shadow: 0 18px 40px rgba(0,0,0,0.45);
    overflow: hidden;
  }
  .header-blocks {
    position: absolute;
    left: 0;
    top: 0;
    width: 672px;
    height: 160px;
  }
  .footer-blocks {
    position: absolute;
    right: 0;
    bottom: 0;
    width: 460px;
    height: 220px;
  }
  .brand {
    position: absolute;
    left: 70px;
    top: 200px;
    display: flex;
    align-items: center;
    gap: 14px;
  }
  .brand-mark {
    width: 34px;
    height: 34px;
    border-radius: 50%;
    background: var(--brand-blue);
  }
  .brand-name {
    font-family: "Exo 2", sans-serif;
    font-weight: 500;
    font-size: 38px;
    letter-spacing: 2px;
    color: var(--brand-blue);
    text-transform: uppercase;
  }
  .contact {
    position: absolute;
    right: 70px;
    top: 190px;
    margin: 0;
    padding: 0;
    list-style: none;
    font-family: "Raleway", sans-serif;
    font-size: 19px;
    line-height: 1.45;
    color: var(--ink);
  }
  .contact-item {
    display: flex;
    align-items: flex-start;
    gap: 12px;
  }
  .contact-icon {
    flex: none;
    width: 18px;
    height: 18px;
    margin-top: 5px;
  }
</style>
</head>
<body>
<main class="canvas">
  <article class="letterhead">
    <svg class="header-blocks" viewBox="0 0 672 160" role="img" aria-label="Overlapping blue square mosaic along the top edge">
      <defs>
        <linearGradient id="headerTone" x1="0" y1="1" x2="1" y2="0">
          <stop offset="0" stop-color="#1b4fa8"/>
          <stop offset="0.55" stop-color="#2a7cc8"/>
          <stop offset="1" stop-color="#5cc0e0"/>
        </linearGradient>
      </defs>
      <polygon fill="url(#headerTone)" points="0,0 672,0 672,22 620,22 620,52 520,52 520,84 400,84 400,112 250,112 250,136 120,136 120,160 0,160"/>
    </svg>

    <div class="brand">
      <span class="brand-mark"></span>
      <span class="brand-name">Bytemill</span>
    </div>

    <ul class="contact">
      <li class="contact-item">
        <svg class="contact-icon" viewBox="0 0 18 18"><circle cx="9" cy="9" r="9" fill="#2d9bd6"/><path d="M6 5.2l1.6-.4 1 2.2-1 .8a5 5 0 0 0 2.6 2.6l.8-1 2.2 1-.4 1.6c-3.6.2-7-3.2-6.8-6.8z" fill="#fff"/></svg>
        <span>+61 400 27 8130</span>
      </li>
      <li class="contact-item">
        <svg class="contact-icon" viewBox="0 0 18 18"><circle cx="9" cy="9" r="9" fill="#2d9bd6"/><path d="M9 4a3 3 0 0 0-3 3c0 2.4 3 6 3 6s3-3.6 3-6a3 3 0 0 0-3-3zm0 4.2a1.2 1.2 0 1 1 0-2.4 1.2 1.2 0 0 1 0 2.4z" fill="#fff"/></svg>
        <span>PO Box 218<br>Northfield SA 5085</span>
      </li>
      <li class="contact-item">
        <svg class="contact-icon" viewBox="0 0 18 18"><circle cx="9" cy="9" r="9" fill="#2d9bd6"/><rect x="4.5" y="6" width="9" height="6.5" rx="0.8" fill="#fff"/><path d="M4.8 6.4L9 9.6l4.2-3.2" stroke="#2d9bd6" stroke-width="1" fill="none"/></svg>
        <span>mail@bytemill.co</span>
      </li>
    </ul>

    <svg class="footer-blocks" viewBox="0 0 460 220" role="img" aria-label="Overlapping blue square mosaic in the bottom right corner">
      <defs>
        <linearGradient id="footerTone" x1="0" y1="1" x2="1" y2="0">
          <stop offset="0" stop-color="#5cc0e0"/>
          <stop offset="0.6" stop-color="#2a8fcf"/>
          <stop offset="1" stop-color="#1f66a8"/>
        </linearGradient>
      </defs>
      <polygon fill="url(#footerTone)" points="460,0 460,220 0,220 0,186 70,186 70,150 170,150 170,112 270,112 270,74 360,74 360,36 420,36 420,0"/>
    </svg>
  </article>
</main>
</body>
</html>
```